Financial Service Company Need Business Card Design

This is a new startup company, first of its kind to offer this service. We facilitate the movement of deposit funds electronically between home buyers and real estate brokerages.Our customers are DOMIVANS®, real estate brokerages, and home buyers, we identify ourselves as a financial/technology company.
Not looking for anything too flashy. Just a clean design that shows the logo, contact info, etc. Company colors can be seen on attached logo, and 'coming soon page'
www.quorvanta.ca

```html
<!DOCTYPE html>
<html lang="en">
<head>
<meta charset="utf-8">
<title>Quorvanta Business Card</title>
<link rel="stylesheet" href="https://fonts.googleapis.com/css2?family=Open+Sans:wght@400;600;700&display=swap">
<style>
  :root {
    --backdrop: #cbcbcb;
    --paper: #ffffff;
    --brand-orange: #f15a2b;
    --ink-grey: #58595b;
    --ink-soft: #6d6e70;
  }
  * { margin: 0; padding: 0; box-sizing: border-box; }
  html, body {
    width: 1105px;
    height: 1200px;
    overflow: hidden;
    background: var(--backdrop);
    font-family: "Open Sans", Arial, sans-serif;
  }
  .stage {
    position: relative;
    width: 1105px;
    height: 1200px;
  }
  .card {
    position: absolute;
    top: 478px;
    width: 440px;
    height: 244px;
    overflow: hidden;
  }
  .card-front { left: 78px; background: var(--paper); }
  .card-back { left: 591px; background: var(--brand-orange); }

  .brand {
    display: flex;
    align-items: center;
    gap: 8px;
    font-weight: 600;
    letter-spacing: -0.3px;
    white-space: nowrap;
  }
  .brand-square {
    width: 18px;
    height: 18px;
    background: var(--brand-orange);
  }
  .card-front .brand {
    position: absolute;
    left: 35px;
    top: 33px;
    font-size: 26px;
    color: var(--ink-grey);
  }
  .holder {
    position: absolute;
    left: 35px;
    top: 133px;
    line-height: 19px;
  }
  .holder-name {
    font-size: 14px;
    font-weight: 700;
    color: var(--brand-orange);
    letter-spacing: 0.4px;
  }
  .holder-role {
    font-size: 14px;
    color: var(--ink-grey);
    letter-spacing: 0.6px;
  }
  .contact {
    position: absolute;
    left: 266px;
    top: 127px;
    list-style: none;
    font-size: 12.5px;
    line-height: 19.3px;
    color: var(--ink-soft);
    letter-spacing: 0.7px;
    white-space: nowrap;
  }

  .card-back .brand {
    position: absolute;
    left: 0;
    right: 0;
    top: 102px;
    justify-content: center;
    font-size: 31px;
    color: var(--paper);
  }
  .card-back .brand-square { background: var(--paper); width: 20px; height: 20px; }
  .web {
    position: absolute;
    left: 0;
    right: 0;
    top: 218px;
    text-align: center;
    font-size: 13px;
    color: var(--paper);
    letter-spacing: 4.2px;
  }
</style>
</head>
<body>
<main class="stage">
  <section class="card card-front">
    <div class="brand"><span class="brand-square"></span>Quorvanta</div>
    <div class="holder">
      <p class="holder-name">xxxx xxxxx</p>
      <p class="holder-role">Director</p>
    </div>
    <ul class="contact">
      <li>xxxx xxxx xxxx</li>
      <li>xxxx xxxx</li>
      <li>P:(555) 555-5555</li>
      <li>F:(555) 555-5555</li>
      <li>hello@quorvanta.ca</li>
    </ul>
  </section>

  <section class="card card-back">
    <div class="brand"><span class="brand-square"></span>Quorvanta</div>
    <p class="web">www.xxxxxxxx.com</p>
  </section>
</main>
</body>
</html>
```